Z-Reel Carnival Podcast Cover Design

We need a podcast cover (square design) for a podcast called Z-Reel Carnival.
MANDATORY: Z-REEL CARNIVAL
OPTIONAL: with The Creature Nerd Dale Furnow

Z-Reel Carnival is a movie podcast dedicated to covering all of the cult oddities you saw in theaters and video stores as a kid but never got to rent or watch. Focusing on obscure horror, cult oddities, action movies, exploitation movies, foreign knockoffs, and more, this a show designed to help you take a trip down memory lane or find new weird movies to add to your streaming queue. Come take a walk on the wild side of cinema at Z-Reel Carnival,..where one person's trash movie is our treasure.
##
Fonts that fit the vibe we're going for:
https://www.typevault.example/sets/grindhouse-drip-font-kelvorn-studio
https://www.pinboardly.example/pin/481926035517204963/
https://www.typevault.example/sets/grindhouse-vintage-font-kelvorn-studio

Target Market(s)

Primarily male, although we have some female fans as well. Podcast fans of B-movies (inexpensively made and a bit outrageous), cult movies, weird movies, old movies, horror movies, and action films.

Industry/Entity Type

Media - Movies -Podcast

Font styles to use
Other font styles liked:
• Fonts that fit the vibe: Fonts: https://www.typevault.example/sets/grindhouse-drip-font-kelvorn-studio https://www.pinboardly.example/pin/481926035517204963/ https://www.typevault.example/sets/grindhouse-vintage-font-kelvorn-studio

Colors
EB3D1F
EC4F4E
F09395
F8D3D4
FCEDEE

Requirements
Must have
• Z-REEL CARNIVAL
Nice to have
• 1) with The Creature Nerd Dale Furnow; 2) VISUALS: VHS tapes

```html
<!DOCTYPE html>
<html lang="en">
<head>
<meta charset="utf-8">
<title>Z-Reel Carnival Podcast Cover</title>
<link rel="stylesheet" href="https://fonts.googleapis.com/css2?family=Saira+Stencil+One&family=Oswald:wght@500;600&family=Permanent+Marker&display=swap">
<style>
  :root {
    --bg-deep: #15171c;
    --bg-mid: #272a31;
    --ink-white: #f4f2ee;
    --label-paper: #ebe7de;
    --tape-black: #121213;
    --tape-edge: #2b2b2d;
    --label-ink: #111111;
    --blood-red: #d3191b;
    --host-tone: #3a3633;
  }
  html, body {
    margin: 0;
    padding: 0;
    overflow: hidden;
    background: var(--bg-deep);
  }
  .cover {
    position: relative;
    width: 1200px;
    height: 1200px;
    overflow: hidden;
    background: linear-gradient(180deg, var(--bg-mid) 0%, var(--bg-deep) 55%, var(--bg-mid) 100%);
  }
  .static-field {
    position: absolute;
    inset: 0;
    background: radial-gradient(ellipse at 50% 40%, #30343c 0%, #1b1d22 70%);
  }
  .podcast-tag {
    position: absolute;
    left: 70px;
    top: 66px;
    font-family: "Oswald", sans-serif;
    font-weight: 600;
    font-size: 27px;
    letter-spacing: 3px;
    color: var(--ink-white);
    display: flex;
    align-items: center;
    gap: 6px;
  }
  .show-title {
    position: absolute;
    left: 0;
    top: 0;
    width: 1200px;
    height: 520px;
    z-index: 2;
  }
  .show-title text {
    font-family: "Saira Stencil One", sans-serif;
    fill: var(--ink-white);
  }
  .host-photo {
    position: absolute;
    left: 342px;
    top: 522px;
    width: 474px;
    height: 374px;
    border-radius: 120px 120px 0 0;
    background: linear-gradient(180deg, #5a4c44 0%, var(--host-tone) 40%, #141414 100%);
  }
  .tape {
    position: absolute;
    background: var(--tape-black);
    border: 3px solid var(--tape-edge);
    box-sizing: border-box;
  }
  .tape-top { left: 216px; top: 894px; width: 726px; height: 102px; }
  .tape-middle { left: 238px; top: 994px; width: 768px; height: 100px; }
  .tape-bottom { left: 192px; top: 1086px; width: 768px; height: 120px; }
  .tape-label {
    position: absolute;
    background: var(--label-paper);
    display: flex;
    align-items: center;
    justify-content: center;
    box-sizing: border-box;
    white-space: nowrap;
  }
  .host-credit {
    left: 346px;
    top: 908px;
    width: 556px;
    height: 78px;
    font-family: "Oswald", sans-serif;
    font-weight: 500;
    font-size: 40px;
    letter-spacing: 3px;
    color: var(--label-ink);
  }
  .host-name {
    left: 442px;
    top: 1010px;
    width: 464px;
    height: 66px;
    font-family: "Permanent Marker", "Comic Sans MS", cursive;
    font-weight: 400;
    font-size: 50px;
    letter-spacing: 1px;
    color: var(--blood-red);
  }
  .bottom-label {
    left: 400px;
    top: 1108px;
    width: 470px;
    height: 72px;
  }
  .spine-number {
    position: absolute;
    font-family: "Oswald", sans-serif;
    font-size: 14px;
    color: var(--label-ink);
    background: var(--label-paper);
    padding: 1px 4px;
  }
</style>
</head>
<body>
<main class="cover">
  <div class="static-field" role="img" aria-label="Dark VHS static and glitch noise background"></div>

  <div class="podcast-tag">
    PODCAST
    <svg width="16" height="20" viewBox="0 0 16 20" aria-hidden="true"><polygon points="2,2 14,10 2,18" fill="#f4f2ee"/></svg>
  </div>

  <svg class="show-title" viewBox="0 0 1200 520" aria-label="Z-Reel Carnival">
    <text x="204" y="296" font-size="178" textLength="792" lengthAdjust="spacingAndGlyphs">Z-REEL</text>
    <text x="204" y="496" font-size="178" textLength="792" lengthAdjust="spacingAndGlyphs">CARNIVAL</text>
  </svg>

  <div class="host-photo" role="img" aria-label="Photo of the bearded host in a black t-shirt wearing a hockey-style mask, seated behind a stack of VHS tapes"></div>

  <div class="tape tape-bottom"></div>
  <div class="tape tape-middle"></div>
  <div class="tape tape-top"></div>

  <span class="spine-number" style="left:232px; top:906px;">009</span>
  <span class="spine-number" style="left:232px; top:930px;">180</span>
  <span class="spine-number" style="left:910px; top:1030px;">195</span>
  <span class="spine-number" style="left:206px; top:1096px;">2</span>
  <span class="spine-number" style="left:206px; top:1150px;">210</span>

  <div class="tape-label host-credit">WITH THE CREATURE NERD</div>
  <div class="tape-label host-name">DALE FURNOW</div>
  <div class="tape-label bottom-label"></div>
</main>
</body>
</html>
```